Sterling Floorworks Letterhead

Letterhead used for business reasons. It must be editable and easy to use.

Address is 5127 W. Harbor Lane Millbrook FL 32099 - 555.382.5519

```html
<!DOCTYPE html>
<html lang="en">
<head>
<meta charset="utf-8">
<title>Sterling Floorworks Letterhead</title>
<link rel="stylesheet" href="https://fonts.googleapis.com/css2?family=Open+Sans:wght@400;600&family=Lexend:wght@500&display=swap">
<style>
  :root {
    --backdrop: #e9eaec;
    --paper: #ffffff;
    --accent: #e08a25;
    --band-grey: #958a85;
    --rule-grey: #9a9392;
    --text: #6e6e6e;
    --text-dark: #3a3a3a;
    --motif: #f3f3f4;
  }
  * { box-sizing: border-box; margin: 0; padding: 0; }
  html, body { width: 999px; height: 1200px; overflow: hidden; background: var(--backdrop); }
  body { position: relative; font-family: "Open Sans", sans-serif; color: var(--text); }

  .letterhead {
    position: absolute; left: 86px; top: 20px;
    width: 827px; height: 1160px;
    background: var(--paper); overflow: hidden;
  }
  .brand {
    position: absolute; top: 82px; left: 0; width: 100%;
    text-align: center; color: var(--accent);
    font-family: "Open Sans", sans-serif; font-weight: 600; font-size: 38px; letter-spacing: 0.5px;
  }
  .header-rules { position: absolute; top: 174px; left: 58px; }

  .sender { position: absolute; left: 74px; top: 251px; }
  .sender-name { color: var(--accent); font-weight: 600; font-size: 22px; line-height: 1.2; }
  .sender-role { font-size: 12.5px; color: var(--text-dark); margin-top: 4px; }
  .contact-list { list-style: none; margin-top: 14px; font-size: 14.5px; color: var(--text-dark); }
  .contact-list li { height: 23.3px; display: flex; align-items: center; }
  .contact-label { color: var(--accent); font-weight: 600; width: 28px; }

  .letter-date { position: absolute; right: 74px; top: 370px; font-size: 14.5px; color: var(--text-dark); }

  .letter-body { position: absolute; left: 75px; top: 443px; width: 678px; font-size: 13.3px; line-height: 21.7px; text-align: justify; }
  .letter-body p + p { margin-top: 21.7px; }

  .signature-area { position: absolute; left: 89px; top: 804px; width: 119px; height: 75px; background: #f4f4f4; }
  .signer-name { position: absolute; left: 75px; top: 888px; font-family: "Lexend", sans-serif; font-weight: 500; font-size: 20px; color: var(--text-dark); }

  .footer-contact { position: absolute; left: 75px; top: 951px; list-style: none; font-size: 12px; color: var(--text); }
  .footer-contact li { display: flex; align-items: center; height: 25px; }
  .footer-contact svg { margin-right: 6px; }

  .footer-motif, .footer-bands { position: absolute; left: 0; top: 0; }
</style>
</head>
<body>
  <main class="letterhead">
    <div class="brand">Sterling Floorworks</div>

    <svg class="header-rules" width="712" height="3" viewBox="0 0 712 3">
      <rect x="0" y="0" width="345" height="2" fill="var(--accent)"/>
      <rect x="351" y="0" width="360" height="2" fill="var(--rule-grey)"/>
    </svg>

    <section class="sender">
      <h1 class="sender-name">James Doe</h1>
      <p class="sender-role">Chief Director</p>
      <ul class="contact-list">
        <li><span class="contact-label">A :</span>2210 Maple Court, Arlington, VA 22201</li>
        <li><span class="contact-label">W :</span>www.companywebsite.com</li>
        <li><span class="contact-label">P :</span>+00 123 456 78</li>
        <li><span class="contact-label">M :</span>companyname@mailbox.com</li>
      </ul>
    </section>

    <p class="letter-date">12 December, 2025</p>

    <section class="letter-body">
      <p>Lorem ipsum dolor sit amet, consectetuer adipiscing elit, sed diam nonummy nibh euismod tincidunt ut laoreet dolore magna aliquam erat volutpat. Ut wisi enim ad minim veniam, quis nostrud exerci tation ullamcorper suscipit lobortis nisl ut aliquip ex ea commodo consequat. Duis autem vel eum iriure dolor in hendrerit in vulputate velit esse molestie consequat, vel illum dolore eu feugiat nulla facilisis at vero eros et accumsan et iusto odio dignissim qui blandit praesent luptatum zzril delenit augue duis dolore te feugait nulla facilisi.</p>
      <p>Lorem ipsum dolor sit amet, cons ectetuer adipiscing elit, sed diam nonummy nibh euismod tincidunt ut laoreet dolore magna aliquam erat volutpat. Ut wisi enim ad minim veniam, quis nostrud exerci tation ullamcorper suscipit lobortis nisl ut aliquip ex ea commodo consequat.</p>
      <p>Lorem ipsum dolor sit amet, consectetuer adipiscing elit, sed diam nonummy nibh euismod tincidunt ut laoreet dolore magna aliquam eratveniam, quis nostrud exerci tation ullamcorper suscipit lobortis nisl ut aliquip ex ea commodo consequat. Lorem ipsum dolor sit zamet, consectetuer adipiscing elit, sed diam nonummy nibh euismod tincidunt.</p>
    </section>

    <div class="signature-area" role="img" aria-label="Handwritten signature"></div>
    <p class="signer-name">Mr. Jone Smith</p>

    <ul class="footer-contact">
      <li>
        <svg width="15" height="15" viewBox="0 0 15 15"><rect width="15" height="15" rx="2" fill="var(--accent)"/><path d="M4.3 3.2l1.6-.2.9 2.2-1 .8c.5 1.2 1.4 2.1 2.6 2.6l.8-1 2.2.9-.2 1.6c-.1.5-.6.8-1.1.7C6.9 10.3 4.7 8.1 4.2 4.9c-.1-.6.2-1.1.7-1.2z" fill="#fff"/></svg>
        555.382.5519
      </li>
      <li>
        <svg width="15" height="15" viewBox="0 0 15 15"><rect width="15" height="15" rx="2" fill="var(--accent)"/><path d="M7.5 2.5a3.4 3.4 0 0 0-3.4 3.4c0 2.5 3.4 6.3 3.4 6.3s3.4-3.8 3.4-6.3A3.4 3.4 0 0 0 7.5 2.5zm0 4.8a1.4 1.4 0 1 1 0-2.8 1.4 1.4 0 0 1 0 2.8z" fill="#fff"/></svg>
        5127 W. Harbor Lane Millbrook FL 32099
      </li>
    </ul>

    <svg class="footer-motif" width="827" height="1160" viewBox="0 0 827 1160" role="img" aria-label="Faint decorative diamond motif">
      <polygon points="413,986 539,1112 491,1160 335,1160 288,1112" fill="var(--motif)"/>
    </svg>

    <svg class="footer-bands" width="827" height="1160" viewBox="0 0 827 1160">
      <polygon points="0,1128 284,1128 296,1141 0,1141" fill="var(--band-grey)"/>
      <polygon points="543,1128 827,1128 827,1141 531,1141" fill="var(--band-grey)"/>
      <polygon points="0,1141 307,1141 323,1160 0,1160" fill="var(--accent)"/>
      <polygon points="522,1141 827,1141 827,1160 505,1160" fill="var(--accent)"/>
    </svg>
  </main>
</body>
</html>
```